Review/Re-Design Supermarket E-Commerce website

We have launched our Supermarket E-commerce Website but feel it is lacking a modern feel.

Please re-design the current Supermarket E-commerce site, creating a more modern look and feel.

I am looking for design changes to things such as:

- Fonts
- Button shape & Size
- Shapes of boxes
- Layout of drop down menus
- A new shopping cart / button
- The Header (and in particular the use and positioning of the logo)
- Supplying a generic background image (currently berries)

Please do not change the structure of the page. For instance, the category selection will always be on the left, the items will always be displayed in rows of 3 and the shopping cart should be on the right.
Updates

Current site can be found at www.brovanmarket.com.au

Project Deadline Extended
Reason: designs coming in are generally too different from current design. we are looking for less that 10% change to the overall look and feel. one aspect that needs a lot of work is the checkout cart on the right hand side. please checkout http://www2.pelkinfreshmart.com.au/?gclid=QXRP4kdmwnLBHTYEzJuaPGEKtB

Target Market(s)

Consumers buying their weekly grocery shopping online

Industry/Entity Type

Shopping

Number of Pages Required

1 page

Requirements
Must have
• Stick to the branding of the Logo. Which is Red, Blue and White.
• Other colours may be used in small percentages.
Should not have
• Do not change the Structure of the site.

```html
<!DOCTYPE html>
<html lang="en">
<head>
<meta charset="utf-8">
<title>Brovan Market – Online Shopping</title>
<link href="https://fonts.googleapis.com/css2?family=Montserrat:wght@400;600;700&family=Roboto:wght@400;500;700&display=swap" rel="stylesheet">
<style>
:root{
  --blue:#0a5fb4;
  --red:#e8232b;
  --orange:#f7941d;
  --green:#4caf2c;
  --green-dark:#1f6e2a;
  --text:#4a4a4a;
  --line:#c9d8e8;
  --topbar:#f1f4f7;
  --footer:#3e4044;
  --footer-base:#333437;
  --footer-text:#8f9297;
}
*{margin:0;padding:0;box-sizing:border-box}
html,body{width:1200px;height:1148px;overflow:hidden;background:#fff}
body{position:relative;font-family:Roboto,Arial,sans-serif;color:var(--text)}
.abs{position:absolute}
.caps{font-family:Montserrat,Arial,sans-serif;text-transform:uppercase;letter-spacing:1px}

.topbar{left:0;top:0;width:1200px;height:25px;background:var(--topbar);border-bottom:1px solid #e3e7eb}
.topbar .phone{left:738px;top:7px;font-size:10px;letter-spacing:.8px;color:#555;display:flex;gap:8px;align-items:center}
.topbar .social{left:835px;top:0;width:113px;height:25px;background:var(--blue);display:flex;justify-content:space-around;align-items:center;padding:0 14px}
.social i{display:block;width:8px;height:8px;background:#fff;border-radius:50%}

.brand{left:251px;top:52px;font-family:Montserrat,Arial,sans-serif;font-weight:700;font-size:15px;color:var(--blue);letter-spacing:.3px;line-height:1;display:flex;align-items:center;gap:8px}
.brand-sub{left:262px;top:68px;font-family:Montserrat,Arial,sans-serif;font-size:9px;letter-spacing:3px;color:#6a6a6a}
.brand .dot{width:12px;height:12px;background:var(--red);border-radius:50%}
.nav{top:58px;font-size:9.5px;color:#444}
.nav.cart{display:flex;gap:8px;align-items:center;top:55px}

.hero{left:0;top:98px;width:1200px;height:212px;background:linear-gradient(90deg,#7d8f4a 0%,#d9a03a 18%,#c9b77a 33%,#e9e4de 45%,#c7b9ab 60%,#d7d0c8 72%,#b8443e 86%,#8fa7c4 100%)}
.tagline{left:398px;top:215px;width:406px;height:45px;background:#fff;font-size:8.5px;font-weight:600;color:var(--blue);text-align:center;line-height:45px;letter-spacing:1.6px}
.finder{left:398px;top:260px;width:406px;height:72px;background:var(--blue)}
.field{top:18px;height:36px;border:2px solid #fff;color:#fff;font-size:8.5px;font-weight:600;display:flex;align-items:center;justify-content:space-between;padding:0 13px}

.side-tab{left:242px;width:129px;height:27px;color:#fff;font-size:8.5px;font-weight:600;display:flex;align-items:center;gap:10px;padding-left:11px}
.specials{top:310px;background:var(--red)}
.favourites{top:337px;background:var(--orange)}
.cats{left:242px;top:374px;list-style:none}
.cats li{height:24.4px;font-size:9px;color:#555;display:flex;align-items:center}
.cats li span{width:13px;color:#777}

.card{width:119px;height:203px;border:1px solid var(--line);background:#fff}
.thumb{left:10px;top:8px;width:97px;height:74px;border-radius:3px}
.pname{left:0;top:89px;width:117px;text-align:center;font-size:10px;letter-spacing:.6px;color:#555}
.rule{left:0;top:114px;width:117px;height:1px;background:var(--line)}
.qty{left:28px;top:125px;width:62px;display:flex;justify-content:space-between;align-items:center;font-size:10px;color:var(--blue);font-weight:500}
.price{left:12px;top:148px;display:flex;gap:5px;align-items:baseline}
.price b{font-size:12.5px;color:var(--blue);letter-spacing:.8px}
.price s{font-size:10px;color:#777;letter-spacing:.6px}
.btn{left:-1px;bottom:-1px;width:119px;height:26px;color:#fff;font-size:8.5px;font-weight:600;display:flex;align-items:center;justify-content:center;gap:8px}
.btn.add{background:var(--blue)}
.btn.added{background:var(--orange)}
.save{left:0;top:0;width:56px;height:56px;background:var(--green);clip-path:polygon(0 0,100% 0,0 100%)}
.save span{position:absolute;left:6px;top:5px;color:#fff;font-size:8px;font-weight:600;line-height:10px;letter-spacing:.6px}

.cartbox{left:830px;top:362px;width:118px;height:478px;border:1px solid var(--line)}
.cartbox .ctr{left:0;width:116px;text-align:center}
.ctitle{font-size:9.5px;color:#3c4a5a;letter-spacing:1.2px}
.addr{font-size:7.5px;line-height:9.5px;color:#444;letter-spacing:.6px}
.cartbox .hr{left:0;width:116px;height:1px;background:var(--line)}
.checkout{left:10px;top:258px;width:98px;height:30px;background:var(--orange);color:#fff;font-size:9px;font-weight:600;display:flex;align-items:center;justify-content:center}
.line-item{left:14px;font-size:7.5px;letter-spacing:.8px;color:#444;line-height:9.5px;width:96px}
.line-price{left:14px;font-size:10px;font-weight:700;color:var(--blue);letter-spacing:.8px}
.remove{left:92px}

.footer{left:0;top:908px;width:1200px;height:179px;background:var(--footer)}
.fcol{top:47px;list-style:none}
.fcol li{font-size:9.5px;letter-spacing:1px;color:var(--footer-text);height:21.5px}
.vline{top:0;width:1px;height:179px;background:#55585c}
.badge{left:845px;width:103px;height:38px;background:#fff;border-radius:3px;border:1px solid #ccc}
.base{left:0;top:1087px;width:1200px;height:61px;background:var(--footer-base)}
.paycard{top:19px;width:34px;height:22px;border-radius:2px}
.copy{left:377px;top:25px;font-size:9px;letter-spacing:1px;color:#75787d}
.bphone{left:668px;top:24px;font-size:10px;color:#cfd1d4;letter-spacing:.8px;display:flex;gap:9px;align-items:center}
.bsocial{top:25px;width:8px;height:8px;background:#b9bcc0;border-radius:50%}
</style>
</head>
<body>

<header>
  <div class="abs topbar">
    <div class="abs phone">
      <svg width="10" height="10" viewBox="0 0 10 10"><path d="M2 0.5l2 2-1 1.3c.6 1.3 1.7 2.4 3 3l1.3-1 2 2-1.3 1.7C4.5 9.5.5 5.5.3 1.8z" fill="#888"/></svg>
      1300 555 204
    </div>
    <div class="abs social" aria-label="Social links"><i></i><i></i><i></i></div>
  </div>

  <div class="abs brand">BROVAN MARKET <span class="dot"></span></div>
  <div class="abs brand-sub">SUPERMARKETS</div>

  <nav>
    <span class="abs nav" style="left:695px">Products</span>
    <span class="abs nav" style="left:771px">Register</span>
    <span class="abs nav" style="left:845px">Login</span>
    <span class="abs nav cart" style="left:893px">
      <svg width="16" height="13" viewBox="0 0 16 13"><path d="M0 1h3l2 8h9l1.5-6H4" fill="none" stroke="#666" stroke-width="1.2"/><circle cx="6" cy="11.5" r="1.2" fill="#666"/><circle cx="13" cy="11.5" r="1.2" fill="#666"/></svg>
      My Cart
    </span>
  </nav>
</header>

<section>
  <div class="abs hero" role="img" aria-label="Shoppers browsing fresh fruit in a supermarket aisle"></div>
  <div class="abs tagline caps">Lorem ipsum is simply dummy text of the printing</div>
  <div class="abs finder">
    <div class="abs field caps" style="left:19px;width:135px">Search
      <svg width="10" height="10" viewBox="0 0 10 10"><circle cx="4" cy="4" r="3" fill="none" stroke="#fff" stroke-width="1.5"/><path d="M6.3 6.3L9 9" stroke="#fff" stroke-width="1.5"/></svg>
    </div>
    <div class="abs field caps" style="left:172px;width:99px">Filter by
      <svg width="8" height="5" viewBox="0 0 8 5"><path d="M1 1l3 3 3-3" fill="none" stroke="#fff" stroke-width="1.2"/></svg>
    </div>
    <div class="abs field caps" style="left:289px;width:99px">Sort by
      <svg width="8" height="5" viewBox="0 0 8 5"><path d="M1 1l3 3 3-3" fill="none" stroke="#fff" stroke-width="1.2"/></svg>
    </div>
  </div>
</section>

<aside>
  <div class="abs side-tab specials caps">
    <svg width="10" height="10" viewBox="0 0 10 10"><path d="M5 0l1.5 3.3 3.5.4-2.6 2.4.7 3.5L5 7.8 1.9 9.6l.7-3.5L0 3.7l3.5-.4z" fill="#f7c21d"/></svg>Online specials
  </div>
  <div class="abs side-tab favourites caps">
    <svg width="11" height="10" viewBox="0 0 11 10"><path d="M1 5l4-4h5v5l-4 4z" fill="none" stroke="#e8232b" stroke-width="1.2"/><circle cx="7.5" cy="3.5" r="1" fill="#e8232b"/></svg>Favourites
  </div>
  <ul class="abs cats">
    <li><span>›</span>Baking Needs</li><li><span>›</span>Baking Accessories</li><li><span>›</span>Beverages</li><li><span>›</span>Coconut</li>
    <li><span>›</span>Biscuits</li><li><span>›</span>Breakfast Foods</li><li><span>›</span>Cereal</li><li><span>›</span>Canned Food</li>
    <li><span>›</span>Baked Beans &amp; Spaghetti</li><li><span>›</span>Cheese</li><li><span>›</span>Blocks</li><li><span>›</span>Chilled Foods</li>
  </ul>
</aside>

<main>
  <article class="abs card" style="left:398px;top:362px">
    <div class="abs thumb" role="img" aria-label="Product photo: bunch of bananas" style="background:linear-gradient(180deg,#fbf1c8,#f3dc84)"></div>
    <div class="abs pname">Bananas Each</div><div class="abs rule"></div>
    <div class="abs qty"><svg width="12" height="12"><circle cx="6" cy="6" r="6" fill="#e8232b"/><path d="M3 6h6" stroke="#fff" stroke-width="1.6"/></svg>6<svg width="12" height="12"><circle cx="6" cy="6" r="6" fill="#1f6e2a"/><path d="M3 6h6M6 3v6" stroke="#fff" stroke-width="1.6"/></svg></div>
    <div class="abs price"><b>$2.99</b><s>$4.67 ea</s></div>
    <div class="abs btn add caps">Add to cart</div>
  </article>
  <article class="abs card" style="left:541px;top:362px">
    <div class="abs thumb" role="img" aria-label="Product photo: red apple" style="background:linear-gradient(180deg,#f6d4d4,#e39a9a)"></div>
    <div class="abs save"><span>SAVE<br>$3.23</span></div>
    <div class="abs pname">Fuji Apples Each</div><div class="abs rule"></div>
    <div class="abs qty"><svg width="12" height="12"><circle cx="6" cy="6" r="6" fill="#e8232b"/><path d="M3 6h6" stroke="#fff" stroke-width="1.6"/></svg>6<svg width="12" height="12"><circle cx="6" cy="6" r="6" fill="#1f6e2a"/><path d="M3 6h6M6 3v6" stroke="#fff" stroke-width="1.6"/></svg></div>
    <div class="abs price"><b>$2.99</b><s>$4.67 ea</s></div>
    <div class="abs btn added caps">Added <svg width="9" height="7"><path d="M1 3.5l2.5 2.5L8 1" fill="none" stroke="#fff" stroke-width="1.2"/></svg></div>
  </article>
  <article class="abs card" style="left:685px;top:362px">
    <div class="abs thumb" role="img" aria-label="Product photo: halved avocado" style="background:linear-gradient(180deg,#e8eccd,#c5cf96)"></div>
    <div class="abs pname">Avocado Each</div><div class="abs rule"></div>
    <div class="abs qty"><svg width="12" height="12"><circle cx="6" cy="6" r="6" fill="#e8232b"/><path d="M3 6h6" stroke="#fff" stroke-width="1.6"/></svg>6<svg width="12" height="12"><circle cx="6" cy="6" r="6" fill="#1f6e2a"/><path d="M3 6h6M6 3v6" stroke="#fff" stroke-width="1.6"/></svg></div>
    <div class="abs price"><b>$2.99</b><s>$4.67 ea</s></div>
    <div class="abs btn add caps">Add to cart</div>
  </article>

  <article class="abs card" style="left:398px;top:592px">
    <div class="abs thumb" role="img" aria-label="Product photo: pile of blueberries" style="background:linear-gradient(180deg,#dde0e8,#aab0c2)"></div>
    <div class="abs pname">Blueberries punnet</div><div class="abs rule"></div>
    <div class="abs qty"><svg width="12" height="12"><circle cx="6" cy="6" r="6" fill="#e8232b"/><path d="M3 6h6" stroke="#fff" stroke-width="1.6"/></svg>6<svg width="12" height="12"><circle cx="6" cy="6" r="6" fill="#1f6e2a"/><path d="M3 6h6M6 3v6" stroke="#fff" stroke-width="1.6"/></svg></div>
    <div class="abs price"><b>$2.99</b><s>$4.67 ea</s></div>
    <div class="abs btn added caps">Added <svg width="9" height="7"><path d="M1 3.5l2.5 2.5L8 1" fill="none" stroke="#fff" stroke-width="1.2"/></svg></div>
  </article>
  <article class="abs card" style="left:541px;top:592px">
    <div class="abs thumb" role="img" aria-label="Product photo: dried dates" style="background:linear-gradient(180deg,#ecdcd8,#c9a8a0)"></div>
    <div class="abs pname">Fuji Apples Each</div><div class="abs rule"></div>
    <div class="abs qty"><svg width="12" height="12"><circle cx="6" cy="6" r="6" fill="#e8232b"/><path d="M3 6h6" stroke="#fff" stroke-width="1.6"/></svg>6<svg width="12" height="12"><circle cx="6" cy="6" r="6" fill="#1f6e2a"/><path d="M3 6h6M6 3v6" stroke="#fff" stroke-width="1.6"/></svg></div>
    <div class="abs price"><b>$2.99</b><s>$4.67 ea</s></div>
    <div class="abs btn add caps">Add to cart</div>
  </article>
  <article class="abs card" style="left:685px;top:592px">
    <div class="abs thumb" role="img" aria-label="Product photo: oranges" style="background:linear-gradient(180deg,#fde8c8,#f5c17c)"></div>
    <div class="abs pname">Avocado Each</div><div class="abs rule"></div>
    <div class="abs qty"><svg width="12" height="12"><circle cx="6" cy="6" r="6" fill="#e8232b"/><path d="M3 6h6" stroke="#fff" stroke-width="1.6"/></svg>6<svg width="12" height="12"><circle cx="6" cy="6" r="6" fill="#1f6e2a"/><path d="M3 6h6M6 3v6" stroke="#fff" stroke-width="1.6"/></svg></div>
    <div class="abs price"><b>$2.99</b><s>$4.67 ea</s></div>
    <div class="abs btn add caps">Add to cart</div>
  </article>
</main>

<aside class="abs cartbox">
  <svg class="abs" style="left:43px;top:17px" width="27" height="27" viewBox="0 0 27 27"><circle cx="13.5" cy="13.5" r="13.5" fill="#1f6e2a"/><rect x="9" y="10" width="9" height="10" fill="#fff"/><path d="M11 10V8.5a2.5 2.5 0 015 0V10" fill="none" stroke="#fff" stroke-width="1.3"/></svg>
  <div class="abs ctr ctitle caps" style="top:51px">Click&amp;Collect</div>
  <div class="abs ctr addr" style="top:67px">Click&amp;Collect<br>12/40 Marlow Street<br>Brovan TAS 7300</div>
  <svg class="abs" style="left:45px;top:113px" width="27" height="27" viewBox="0 0 27 27"><circle cx="13.5" cy="13.5" r="13.5" fill="#0a5fb4"/><rect x="6" y="10" width="9" height="7" fill="#fff"/><path d="M15 12h3.5l2.5 3v2h-6z" fill="#fff"/><circle cx="9" cy="18" r="1.5" fill="#fff"/><circle cx="18" cy="18" r="1.5" fill="#fff"/></svg>
  <div class="abs ctr ctitle caps" style="top:147px">Delivery info</div>
  <div class="abs hr" style="top:182px"></div>

  <svg class="abs" style="left:10px;top:199px" width="22" height="18" viewBox="0 0 22 18"><path d="M0 1h4l3 11h11l2.5-8H5.5" fill="none" stroke="#0a5fb4" stroke-width="1.5"/><path d="M7 6.5h12M7.8 9h10.5" stroke="#0a5fb4" stroke-width="1"/><circle cx="8.5" cy="15.5" r="1.6" fill="#0a5fb4"/><circle cx="16.5" cy="15.5" r="1.6" fill="#0a5fb4"/></svg>
  <div class="abs" style="left:43px;top:202px;font-size:10.5px;letter-spacing:1px;color:#555">3 items</div>
  <div class="abs caps" style="left:10px;top:233px;font-size:7.5px;color:#444">Sub total</div>
  <div class="abs" style="left:69px;top:231px;font-size:11.5px;font-weight:700;color:var(--blue);letter-spacing:.8px">$24.00</div>
  <div class="abs checkout caps">Checkout</div>
  <div class="abs hr" style="top:307px"></div>

  <div class="abs line-item" style="top:319px">1x ROSY CRISP Apples Each</div>
  <div class="abs line-price" style="top:344px">$0.60</div>
  <svg class="abs remove" style="top:344px" width="12" height="12"><circle cx="6" cy="6" r="5.3" fill="none" stroke="#9fb6cf"/><path d="M4 4l4 4M8 4l-4 4" stroke="#9fb6cf"/></svg>
  <div class="abs hr" style="top:365px"></div>

  <div class="abs line-item" style="top:378px">1x Fuji Apples Each</div>
  <div class="abs line-price" style="top:398px">$0.60</div>
  <svg class="abs remove" style="top:398px" width="12" height="12"><circle cx="6" cy="6" r="5.3" fill="none" stroke="#9fb6cf"/><path d="M4 4l4 4M8 4l-4 4" stroke="#9fb6cf"/></svg>
  <div class="abs hr" style="top:420px"></div>

  <div class="abs line-item" style="top:432px">1x Fuji Apples Each</div>
  <div class="abs line-price" style="top:452px">$0.60</div>
  <svg class="abs remove" style="top:452px" width="12" height="12"><circle cx="6" cy="6" r="5.3" fill="none" stroke="#9fb6cf"/><path d="M4 4l4 4M8 4l-4 4" stroke="#9fb6cf"/></svg>
</aside>

<footer>
  <div class="abs footer">
    <ul class="abs fcol" style="left:253px"><li>My Account</li><li>My Past Orders</li><li>Online Specials</li><li>Everyday Specials</li></ul>
    <div class="abs vline" style="left:402px"></div>
    <ul class="abs fcol" style="left:460px"><li>Delivery</li><li>FAQ</li><li>Privacy Policy</li><li>Terms &amp; Conditions</li></ul>
    <div class="abs vline" style="left:612px"></div>
    <ul class="abs fcol" style="left:667px"><li>About Quayline</li><li>About Us</li><li>End User License</li><li>Agreement</li></ul>
    <div class="abs badge" style="top:42px" aria-label="App store badge"></div>
    <div class="abs badge" style="top:87px" aria-label="App store badge"></div>
  </div>
  <div class="abs base">
    <div class="abs paycard" style="left:250px;background:#d9dde2"></div>
    <div class="abs paycard" style="left:289px;background:#eceef0"></div>
    <div class="abs paycard" style="left:328px;background:#f4f5f7"></div>
    <div class="abs copy">© Quayline Pty Ltd 2014 · All Rights Reserved ver 1.1.5</div>
    <div class="abs bphone">
      <svg width="10" height="10" viewBox="0 0 10 10"><path d="M2 0.5l2 2-1 1.3c.6 1.3 1.7 2.4 3 3l1.3-1 2 2-1.3 1.7C4.5 9.5.5 5.5.3 1.8z" fill="#cfd1d4"/></svg>
      1300 555 204
    </div>
    <i class="abs bsocial" style="left:858px"></i>
    <i class="abs bsocial" style="left:886px"></i>
    <i class="abs bsocial" style="left:917px"></i>
  </div>
</footer>

</body>
</html>
```